"Crestline Shape Trim Method" eBook cover

THE TITLE HAS CHANGED SLIGHTLY TO ;
"Crestline Shape Trim Method"

The following is for a fat loss, health and fitness eBook titled "Crestline Shape Trim Method." This design should help promote and market this product, as well as intrigue those to not only make a purchase... but want to very much participate in the material and follow the material!

There is no restriction of color, idea, etc. PLEASE help me with your expertise in developing a great cover for this project...

THANKS SO MUCH

This book separates others just by the quality information provided. To much trial and error is wasted on false claims and overrated programs....I have provided the books topics below to hopefully give you a better understanding;
CHAPTER 1
Crestline Shape Trim Guide
- What is it?
- Why it works?
- Why it will work for you?
CHAPTER 2
Kill Cardio
- Why cardio sucks?
- Myth about cardio?
- What cardio works for fat loss
CHAPTER 3
Iron vs. Machine
- What type of resistance training is best for fat loss?
- Why?
- The big pitfall to working on machines?
CHAPTER 4
Should You Really Eat That?
- Foods that build muscle
- Foods that burn fat
- Foods that suck!
CHAPTER 5
Playing With Iron
- Playing with iron
- 17 upper body builders
- 17 lower body builders
- 11 workouts in 11 minutes
CHAPTER 6
Buying Equipment On A Budget
- How to find dirt cheap dumbbells?
- How to build equipment under $100

THANKS AGAIN!

Target Market(s)

Self-Help / Health And Fitness / Nutrition

Industry/Entity Type

Health And Wellness

Font styles to use
Serif
Sans Serif
Other font styles liked:
• Tahoma, Verdana, Calibri

Requirements
Must have
• MUST MEET VORELLO.com GUIDLINES ;
• File Types
• Pagewell Direct Publishing currently accepts two types of files for cover images:
• JPEG (JPEG / JPG)
• TIFF (TIF / TIFF)
• We apply additional compression to images when displaying them on the website. For best results, please upload your images with minimal compression.
• Dimensions
• Requirements for the size of your cover art must have an ideal height/width ratio of at least 8:5 (1.6), meaning:
• • A minimum of 625 pixels on the shortest side and 1000 pixels on the longest side
• • For best quality, your image should be 2500 pixels on the longest side
• Important: We cannot accept any images larger than 10,000 pixels on the longest side.
• Size
• Your cover image must be less than 50MB. If the file type you are using supports compression, make sure to enable as little compression as possible, e.g. none for TIFF. Be sure to save your file with 72 dots per inch (DPI).
• Color
• Product images display on the Vorello website using the RGB (red, green, blue) color mode or profile. RGB is the color mode native to the web and many color screen displays, as these three colors displayed at varying levels of intensity create over 16 million colors. When saving and uploading your cover image file, save your file ONLY as RGB - not CMYK or sRGB- for the color profile. You can usually find this option in the File saving dialog of image manipulation programs such as Photoshop.
• Some programs may also refer to RGB color as 'True Color' in some programs. If in doubt, try opening a JPG inside Internet Explorer, Firefox, or Safari. If a JPG opens fine inside a web browser, it's most likely okay to use as a cover image.
• Make sure to save your image without color separation. This is usually a pre-press or color palette option. Use your image manipulation program or image analysis tool (some are available free online) to verify that your image file doesn't have color separation.
• Use color images whenever possible and relevant. In addition to the Pagewell black and white E Ink reading devices, customers can read your books on full color Lumo devices and free Pagewell reading apps for iPhone, iPad, Android, PC or Mac.
Should not have
• NO MALE OR FEMALE MODLES OR HALF NAKED PEOPLE...

```html
<!DOCTYPE html>
<html lang="en">
<head>
<meta charset="utf-8">
<title>Crestline Shape Trim Method — Cover</title>
<link rel="stylesheet" href="https://fonts.googleapis.com/css2?family=Source+Sans+3:wght@600;700;800&display=swap">
<style>
  :root {
    --stage: #e9e8e4;
    --navy: #0d0e22;
    --navy-soft: #1b1d3a;
    --paper: #ffffff;
    --lime: #c9d770;
    --steel: #8e968c;
    --ink: #0d0e22;
  }
  * { margin: 0; padding: 0; box-sizing: border-box; }
  html, body {
    width: 1200px;
    height: 960px;
    overflow: hidden;
    background: var(--stage);
    font-family: "Source Sans 3", "Segoe UI", sans-serif;
  }
  .book-cover {
    position: absolute;
    left: 280px;
    top: 48px;
    width: 640px;
    height: 864px;
    background: var(--paper);
    overflow: hidden;
    box-shadow: 0 10px 30px rgba(0,0,0,0.18);
  }
  .cover-split {
    position: absolute;
    inset: 0;
    width: 100%;
    height: 100%;
  }
  .title-block {
    position: absolute;
    top: 92px;
    right: 40px;
    text-align: right;
    color: var(--paper);
    text-transform: uppercase;
  }
  .title-line { display: block; }
  .title-kicker {
    font-weight: 700;
    font-size: 34px;
    letter-spacing: 0.32em;
    margin-right: -0.32em;
    line-height: 1;
  }
  .title-accent {
    font-weight: 700;
    font-size: 112px;
    line-height: 0.95;
    color: var(--lime);
    margin-top: 14px;
  }
  .title-main {
    font-weight: 800;
    font-size: 112px;
    line-height: 0.95;
    color: var(--paper);
  }
  .equipment-art {
    position: absolute;
    left: 70px;
    top: 510px;
    width: 500px;
    height: 265px;
    border-radius: 18px;
    background: radial-gradient(ellipse at center, #e4ebbf 0%, #eef1e2 55%, #f6f7f2 100%);
  }
  .author-name {
    position: absolute;
    left: 0;
    right: 0;
    bottom: 38px;
    text-align center;
    text-align: center;
    font-weight: 700;
    font-size: 24px;
    letter-spacing: 0.04em;
    color: var(--ink);
    text-transform: uppercase;
  }
</style>
</head>
<body>
  <main class="book-cover">
    <svg class="cover-split" viewBox="0 0 640 864" preserveAspectRatio="none" aria-hidden="true">
      <defs>
        <linearGradient id="navyBand" x1="0" y1="0" x2="1" y2="0">
          <stop offset="0" stop-color="#1b1d3a"/>
          <stop offset="0.5" stop-color="#0d0e22"/>
          <stop offset="1" stop-color="#07081a"/>
        </linearGradient>
      </defs>
      <polygon points="0,0 640,0 640,395 0,495" fill="url(#navyBand)"/>
    </svg>

    <h1 class="title-block">
      <span class="title-line title-kicker">Crestline Shape</span>
      <span class="title-line title-accent">Trim</span>
      <span class="title-line title-main">Method</span>
    </h1>

    <div class="equipment-art" role="img" aria-label="Line illustration of gym equipment arranged symmetrically: weight plate, barbells, dumbbells, kettlebells, hand grips and resistance bands in lime green and grey"></div>

    <p class="author-name">Dario Venhall</p>
  </main>
</body>
</html>
```